New B2C website design to help dads be better dads

KinHarbor is a website to help dads be the “best dad you can be.”

We require our website to be designed into a PSD format, no coding necessary.

The general concept is a two-page design. The first page is the login page, the second page is the home page. Once at the home page, rather than navigating to and from different pages, the user will push and pull through different visual and functional layers of the hierarchy. In theory, this should add to the user experience by having a visual anchor of where they are (through layered pagination) as well as improving loading times since the new information should only be a delta in data load versus a brand new page load.

The general look-and-feel we are going for is clean, simple, minimal. This means that the winning design will show us a good eye for web-optimized typography, good use of white (negative) space, and good use of a visually pleasing grid.

We require a total of 6 page "views" plus the landing page. We note that many of the views are similar to one another.
Landing page
Milestone view
Task view
Content view, articles
Content view, products
Search view
What's new view

Please review all of the additional information provided as well as the attachments for examples.

We provide the following websites as good references for:

Typography:
http://quillbrenner.com/journal/

Use of white space:
http://www.dotlantern.com/
http://tidekiosk.com/

Example for “scrolling” page concept as well as good balance of color, typography, and white space:
http://www.morvensummit.eu/

Please contact us with questions so that we can guide your design effort.
Updates

Hello designers,

The following information is added to help guide the design process:

1.  For the text dialogue below the landing page, please assume the following word count:
"why are we making kin harbor?": 250 words
"who are we?" 200 words
"what's the deal with the penguin logo?" 300 words

For the social media links, please see http://www.glowberrycritics.com/
Notice the floating "social" bar that is always to the right.  This is the concept we are going for, please try to implement this as you see fit. 

Reason: Final design requests have been sent out to finalist designers, want to give everyone time to do a good job.

Target Market(s)

Fathers of young children ages 0-6 years old.

Industry/Entity Type

Product

Font styles to use
Sans Serif

Requirements
Must have
• Clean lines, minimal design concept

Incorporation of our logo (see attached document)

Header content is static for all views after landing page, see example

This page WILL be responsive, please keep that in mind when designing
The timeline bar should be to the left, with the timeline bar’s “milestones” also being responsive.

Designer is free to suggest font types, but any fonts used must be royalty-free and web-optimized. We request a minimum number of font types as well as fonts that load relatively fast. We reinforce that visually appealing typography is a significant factor in the winning design choice.

While we are not expecting the winning design to include code, please keep in mind that the final implementation needs to be optimized for desktop, tablet, and mobile platforms.

If you are using stock photography that is not generated by you, please provide where/how we can obtain imagery, as well as price.

All custom graphics must be available in original formats; Photoshop/GIMP layered files for layout design, and vector formats for logos, icons and other graphical elements.

Please incorporate “Blue” into design elements as you see fit, as the RGB 67 74 169 Blue is the primary color used in our brand. The complement to this blue is 255 202 0, a brownish orange. Feel free to use this color as well, although please keep it to a lesser amount.

Background color is your choice, do not feel the need to use the grey.
Should not have
• Excessive graphical content such that it affects loading times

Excessive use of too many font types such that it affects loading times

```html
<!DOCTYPE html>
<html lang="en">
<head>
<meta charset="utf-8">
<title>KinHarbor – Prepare for the baby arrival</title>
<link rel="stylesheet" href="https://fonts.googleapis.com/css2?family=Crimson+Text:wght@400&family=Source+Sans+3:wght@300;400;600&display=swap">
<style>
:root{
  --brand-blue:#434aa9;
  --title-blue:#2e3595;
  --footer-blue:#2c3190;
  --footer-deep:#262a80;
  --sun:#ffca00;
  --sun-dark:#f3b400;
  --ink:#444;
  --muted:#8a8a8a;
  --line:#dcdcdc;
  --page:#ffffff;
}
*{box-sizing:border-box;margin:0;padding:0}
html,body{width:822px;height:1200px;overflow:hidden;background:var(--page)}
body{position:relative;font-family:"Source Sans 3",Arial,sans-serif;color:var(--ink)}

.site-header{position:absolute;left:0;top:0;width:822px;height:120px;background:linear-gradient(#fdfdfd,#f3f3f3);border-bottom:1px solid #eee}
.brand{position:absolute;left:50px;top:76px;display:flex;align-items:center;gap:6px;font-size:13px;font-weight:600;color:var(--brand-blue);letter-spacing:.3px}
.brand-dot{width:10px;height:10px;border-radius:50%;background:var(--brand-blue)}
.welcome{position:absolute;left:199px;top:38px;font-family:"Crimson Text",Georgia,serif;font-size:20px;color:var(--title-blue)}
.score{position:absolute;left:201px;top:79px;font-size:11px;color:#555}
.btn-search{position:absolute;left:324px;top:72px;width:79px;height:24px;border-radius:2px;background:linear-gradient(var(--sun),var(--sun-dark));color:#fff;font-size:12px;font-weight:600;display:flex;align-items:center;justify-content:center}
.account{position:absolute;left:640px;top:65px;font-size:11px;color:#777}
.btn-logout{position:absolute;left:708px;top:62px;width:60px;height:22px;border-radius:2px;background:var(--title-blue);color:#fff;font-size:9px;font-weight:600;display:flex;align-items:center;justify-content:center}

.page-title{position:absolute;left:42px;top:144px;font-size:21px;font-weight:300;color:#555}
.sort{position:absolute;left:662px;top:148px;width:92px;height:24px;border:1px solid #d8d8d8;border-radius:2px;background:#fff;font-size:9.5px;color:#666;display:flex;align-items:center;padding-left:11px}
.sort svg{position:absolute;right:8px;top:9px}

.tasks{position:absolute;left:41px;top:189px;width:190px;height:221px;border:1px solid var(--line);border-radius:2px;background:linear-gradient(#fff,#f3f3f3);list-style:none;padding-top:18px}
.tasks li{display:flex;align-items:center;height:22.9px;padding-left:20px;font-size:10.5px;font-weight:300;color:#555}
.check{width:14px;height:14px;border:1px solid #d6d6d6;border-radius:2px;background:#f7f7f7;margin-right:9px;display:flex;align-items:center;justify-content:center}

.grid{position:absolute;left:266px;top:190px;display:grid;grid-template-columns:234px 233px;column-gap:21px;row-gap:26px}
.card{height:230px;border:1px solid var(--line);border-radius:2px;background:linear-gradient(#fff 60%,#f3f3f3);overflow:hidden}
.card-photo{height:118px}
.card-body{padding:10px 16px 0}
.card-title{font-size:14.5px;font-weight:400;color:var(--title-blue);white-space:nowrap}
.rating{display:flex;align-items:center;gap:1px;margin-top:4px;font-size:9.5px;color:var(--title-blue)}
.rating span{margin-left:8px}
.card-text{margin-top:6px;font-size:8.6px;line-height:14.5px;font-weight:300;color:#777}

.site-footer{position:absolute;left:0;top:968px;width:822px;height:182px;background:var(--footer-blue)}
.foot-col{position:absolute;top:30px}
.foot-col h3{font-size:15px;font-weight:400;color:#fff;margin-bottom:5px}
.foot-col a{display:block;font-size:10px;line-height:17.4px;color:#e4e6ff;text-decoration:none;margin-left:1px}
.divider{position:absolute;top:30px;width:1px;height:117px;background:#444ab0}
.social{display:flex;gap:4px;margin-top:4px}
.social i{display:block;width:20px;height:20px;border-radius:50%;background:#fff}
.legal{position:absolute;left:0;top:1150px;width:822px;height:50px;background:var(--footer-deep);font-size:9.5px;color:#6c72c4;padding:16px 0 0 48px}
</style>
</head>
<body>
<header class="site-header">
  <div class="brand"><span class="brand-dot"></span>KINHARBOR</div>
  <h1 class="welcome">Welcome Greg, What would you like to do today?</h1>
  <p class="score">Super Dad Score: 10,500</p>
  <a class="btn-search">Search</a>
  <a class="account">My Account</a>
  <a class="btn-logout">LOGOUT</a>
</header>

<h2 class="page-title">Prepare for the baby arrival</h2>
<div class="sort">Most Viewed
  <svg width="8" height="5" viewBox="0 0 8 5"><path d="M0 0h8L4 5z" fill="#555"/></svg>
</div>

<svg width="0" height="0" style="position:absolute">
  <symbol id="star" viewBox="0 0 10 10"><path d="M5 .4l1.4 3 3.2.3-2.4 2.1.7 3.2L5 7.4 2.1 9l.7-3.2L.4 3.7l3.2-.3z"/></symbol>
  <symbol id="tick" viewBox="0 0 10 10"><path d="M1.5 5.2l2.4 2.4 4.6-5" fill="none" stroke="#444" stroke-width="1.4"/></symbol>
</svg>

<ul class="tasks">
  <li><span class="check"></span>Buy a crib</li>
  <li><span class="check"></span>Assemble the crib</li>
  <li><span class="check"></span>Buy a stroller</li>
  <li><span class="check"><svg width="10" height="10"><use href="#tick"/></svg></span>Buy a carseat</li>
  <li><span class="check"></span>Install a carseat</li>
  <li><span class="check"></span>Learn to change a diaper</li>
  <li><span class="check"></span>Learn to hold a baby</li>
  <li><span class="check"></span>Set a feeding schedule</li>
</ul>

<main class="grid">
  <article class="card">
    <div class="card-photo" role="img" aria-label="Parent buckling a baby into a car seat" style="background:linear-gradient(120deg,#c9485a,#e2b7a4 50%,#3b3b3b)"></div>
    <div class="card-body"><h3 class="card-title">Cum sociis natoque</h3>
      <div class="rating"><svg width="12" height="12" fill="#ffca00"><use href="#star"/></svg><svg width="12" height="12" fill="#ffca00"><use href="#star"/></svg><svg width="12" height="12" fill="#ffca00"><use href="#star"/></svg><svg width="12" height="12" fill="#ffca00"><use href="#star"/></svg><svg width="12" height="12" fill="#f5e4a0"><use href="#star"/></svg><span>3,121 Ratings</span></div>
      <p class="card-text">Morbi diam mauris, viverra in, gravida eu, mattis in, ante. Morbi eget arcu. Morbi porta, libero id ullam-corper nonummy, nibh ligula pulvinar</p></div>
  </article>
  <article class="card">
    <div class="card-photo" role="img" aria-label="Baby in a red car seat with green knit hat" style="background:linear-gradient(120deg,#8b7a5e,#e6dccf 50%,#c9303a)"></div>
    <div class="card-body"><h3 class="card-title">Etiam est nunc venenatis</h3>
      <div class="rating"><svg width="12" height="12" fill="#ffca00"><use href="#star"/></svg><svg width="12" height="12" fill="#ffca00"><use href="#star"/></svg><svg width="12" height="12" fill="#ffca00"><use href="#star"/></svg><svg width="12" height="12" fill="#ffca00"><use href="#star"/></svg><svg width="12" height="12" fill="#f5e4a0"><use href="#star"/></svg><span>3,121 Ratings</span></div>
      <p class="card-text">Morbi diam mauris, viverra in, gravida eu, mattis in, ante. Morbi eget arcu. Morbi porta, libero id ullam-corper nonummy, nibh ligula pulvinar</p></div>
  </article>
  <article class="card">
    <div class="card-photo" role="img" aria-label="Toddler smiling in a car seat by the window" style="background:linear-gradient(120deg,#4d6b35,#b9ad98 45%,#5a3a33)"></div>
    <div class="card-body"><h3 class="card-title">Donec scelerisque leo ac risus</h3>
      <div class="rating"><svg width="12" height="12" fill="#ffca00"><use href="#star"/></svg><svg width="12" height="12" fill="#ffca00"><use href="#star"/></svg><svg width="12" height="12" fill="#ffca00"><use href="#star"/></svg><svg width="12" height="12" fill="#ffca00"><use href="#star"/></svg><svg width="12" height="12" fill="#f5e4a0"><use href="#star"/></svg><span>3,121 Ratings</span></div>
      <p class="card-text">Morbi diam mauris, viverra in, gravida eu, mattis in, ante. Morbi eget arcu. Morbi porta, libero id ullam-corper nonummy, nibh ligula pulvinar</p></div>
  </article>
  <article class="card">
    <div class="card-photo" role="img" aria-label="Infant lying in a blue car seat" style="background:linear-gradient(120deg,#2e3f4d,#8a9aa5 50%,#2f8fc7)"></div>
    <div class="card-body"><h3 class="card-title">Praesent sit amet est</h3>
      <div class="rating"><svg width="12" height="12" fill="#ffca00"><use href="#star"/></svg><svg width="12" height="12" fill="#ffca00"><use href="#star"/></svg><svg width="12" height="12" fill="#ffca00"><use href="#star"/></svg><svg width="12" height="12" fill="#ffca00"><use href="#star"/></svg><svg width="12" height="12" fill="#f5e4a0"><use href="#star"/></svg><span>3,121 Ratings</span></div>
      <p class="card-text">Morbi diam mauris, viverra in, gravida eu, mattis in, ante. Morbi eget arcu. Morbi porta, libero id ullam-corper nonummy, nibh ligula pulvinar</p></div>
  </article>
  <article class="card">
    <div class="card-photo" role="img" aria-label="Baby in a striped hat seated in the back of a car" style="background:linear-gradient(120deg,#3a3a3a,#cfc9c0 50%,#4a4a4a)"></div>
    <div class="card-body"><h3 class="card-title">Vivamus porttitor purus</h3>
      <div class="rating"><svg width="12" height="12" fill="#ffca00"><use href="#star"/></svg><svg width="12" height="12" fill="#ffca00"><use href="#star"/></svg><svg width="12" height="12" fill="#ffca00"><use href="#star"/></svg><svg width="12" height="12" fill="#ffca00"><use href="#star"/></svg><svg width="12" height="12" fill="#f5e4a0"><use href="#star"/></svg><span>3,121 Ratings</span></div>
      <p class="card-text">Morbi diam mauris, viverra in, gravida eu, mattis in, ante. Morbi eget arcu. Morbi porta, libero id ullam-corper nonummy, nibh ligula pulvinar</p></div>
  </article>
  <article class="card">
    <div class="card-photo" role="img" aria-label="Laughing baby strapped into a grey car seat" style="background:linear-gradient(120deg,#2f2f2f,#9a9590 50%,#5f6a70)"></div>
    <div class="card-body"><h3 class="card-title">Praesent elementum elit at tellus</h3>
      <div class="rating"><svg width="12" height="12" fill="#ffca00"><use href="#star"/></svg><svg width="12" height="12" fill="#ffca00"><use href="#star"/></svg><svg width="12" height="12" fill="#ffca00"><use href="#star"/></svg><svg width="12" height="12" fill="#ffca00"><use href="#star"/></svg><svg width="12" height="12" fill="#f5e4a0"><use href="#star"/></svg><span>3,121 Ratings</span></div>
      <p class="card-text">Morbi diam mauris, viverra in, gravida eu, mattis in, ante. Morbi eget arcu. Morbi porta, libero id ullam-corper nonummy, nibh ligula pulvinar</p></div>
  </article>
</main>

<footer class="site-footer">
  <nav class="foot-col" style="left:57px"><h3>Company</h3><a>Cum sociis</a><a>Natoque penatibus</a><a>Magnis dis parturient</a><a>Montes nascetur</a><a>Ridiculus mus</a></nav>
  <span class="divider" style="left:166px"></span>
  <nav class="foot-col" style="left:194px"><h3>Services</h3><a>Services Provide</a><a>Natoque penatibus</a><a>Montes nascetur</a><a>Ridiculus mus</a></nav>
  <span class="divider" style="left:307px"></span>
  <nav class="foot-col" style="left:329px"><h3>Support</h3><a>Customer Service</a><a>Legal</a><a>Sitemap</a><a>Resources</a></nav>
  <span class="divider" style="left:422px"></span>
  <nav class="foot-col" style="left:448px"><h3>Sublinks</h3><a>Services Provide</a><a>Natoque penatibus</a><a>Montes nascetur</a><a>Ridiculus mus</a></nav>
  <span class="divider" style="left:558px"></span>
  <div class="foot-col" style="left:587px"><h3>Get Connected</h3><div class="social"><i></i><i></i><i></i><i></i></div></div>
</footer>
<div class="legal">© 2013 Company Name. &nbsp;All right reserved. &nbsp;Term of Use</div>
</body>
</html>
```